Banner design

I need a banner designed that we will be putting on our gym walls. We need two banners but both will have the same design:
- One will be printed 12.2 X 2.5m
- One will be printed 9.4 X 2.5m
We are a kids gymnastics and cheerleading gym so are looking for something bright and fun that still looks professional.
Our colours are lime green, navy blue and white.
I have uploaded a couple of examples of what other gyms have done.
Kids

```html
<!DOCTYPE html>
<html lang="en">
<head>
<meta charset="utf-8">
<title>Starleap Gymsports – Wall Banner</title>
<link href="https://fonts.googleapis.com/css2?family=Exo+2:wght@800&family=Roboto+Condensed:wght@400&display=swap" rel="stylesheet">
<style>
  :root {
    --navy: #1b2d52;
    --lime: #b5e12a;
    --paper: #eeeeef;
    --stage: #e4e4e4;
    --ink: #2a2f3a;
  }
  html, body {
    margin: 0;
    padding: 0;
    overflow: hidden;
  }
  body {
    width: 934px;
    height: 1200px;
    background: var(--stage);
    position: relative;
  }
  .banner {
    position: absolute;
    left: 27px;
    top: 483px;
    width: 880px;
    height: 234px;
    background: var(--paper);
    box-shadow: 4px 5px 8px rgba(0,0,0,0.28);
    overflow: hidden;
  }
  .banner__art {
    position: absolute;
    inset: 0;
    width: 100%;
    height: 100%;
  }
  .apparel {
    position: absolute;
    left: 26px;
    top: 14px;
    width: 90px;
    height: 172px;
    border-radius: 4px;
    background: linear-gradient(180deg, #c2433e 0%, #c2433e 45%, #1d1f28 55%, #25305a 100%);
  }
  .brand {
    position: absolute;
    left: 200px;
    top: 0;
    width: 330px;
    height: 150px;
    margin: 0;
    font-family: "Exo 2", sans-serif;
    font-weight: 800;
    color: var(--navy);
    line-height: 1;
    text-align: center;
  }
  .brand__name {
    position: absolute;
    left: 0;
    right: 0;
    top: 30px;
    font-size: 58px;
    letter-spacing: 1px;
    white-space: nowrap;
  }
  .brand__mark {
    display: inline-block;
    width: 16px;
    height: 16px;
    border-radius: 50%;
    background: var(--lime);
    vertical-align: middle;
    margin-right: 8px;
  }
  .brand__sub {
    position: absolute;
    left: 0;
    right: 0;
    top: 118px;
    font-size: 25px;
    letter-spacing: 4px;
    white-space: nowrap;
  }
  .blurb {
    position: absolute;
    left: 225px;
    top: 156px;
    width: 280px;
    margin: 0;
    text-align: center;
    font-family: "Roboto Condensed", sans-serif;
    font-weight: 400;
    font-size: 8px;
    line-height: 1.3;
    color: var(--ink);
  }
  .follow {
    position: absolute;
    left: 315px;
    top: 196px;
    width: 100px;
    text-align: center;
    font-family: "Roboto Condensed", sans-serif;
    font-weight: 400;
    font-size: 8.5px;
    line-height: 1;
    color: var(--navy);
  }
  .follow__links {
    display: flex;
    justify-content: center;
    gap: 9px;
    margin-top: 4px;
  }
  .follow__dot {
    width: 13px;
    height: 13px;
    border-radius: 2px;
    background: var(--navy);
  }
</style>
</head>
<body>
  <section class="banner">
    <svg class="banner__art" viewBox="0 0 1070 285" preserveAspectRatio="none" aria-hidden="true">
      <defs>
        <linearGradient id="band-fade" x1="0" x2="1" y1="0" y2="0">
          <stop offset="0" stop-color="#1b2d52"/>
          <stop offset="0.3" stop-color="#1b2d52" stop-opacity="0.6"/>
          <stop offset="0.6" stop-color="#1b2d52" stop-opacity="0.12"/>
          <stop offset="1" stop-color="#1b2d52" stop-opacity="0"/>
        </linearGradient>
      </defs>
      <polygon points="0,0 70,0 30,130 0,150" fill="#1b2d52"/>
      <rect x="0" y="245" width="720" height="40" fill="url(#band-fade)"/>
      <polygon points="985,0 1070,0 1070,285 880,285" fill="#1b2d52"/>
      <circle cx="840" cy="140" r="150" fill="none" stroke="#b5e12a" stroke-width="20"/>
      <circle cx="840" cy="140" r="120" fill="#eeeeef"/>
    </svg>

    <div class="apparel" role="img" aria-label="Product photos of gym apparel: red top, sports bra, leggings, black singlet and navy unitard"></div>

    <svg class="banner__art" viewBox="0 0 1070 285" preserveAspectRatio="none">
      <circle cx="860" cy="140" r="110" fill="#e9c9b4" role="img" aria-label="Photo of a young gymnast in a teal leotard performing a backbend"/>
    </svg>

    <h1 class="brand">
      <span class="brand__name"><span class="brand__mark"></span>STARLEAP</span>
      <span class="brand__sub">GYMSPORTS</span>
    </h1>

    <p class="blurb">Neque porro quisquam est qui dolorem ipsum quia dolor sit amet, consectetur, adipisci velitNeque porro quisquam est qui dolorem ipsum quia dolor sit amet, consectetur, adipisci velit</p>

    <div class="follow">
      FOLLOW US
      <div class="follow__links">
        <span class="follow__dot"></span>
        <span class="follow__dot"></span>
        <span class="follow__dot"></span>
      </div>
    </div>
  </section>
</body>
</html>
```